Velmora Partners - website for real estate investment company

Create a bold, modern website that reflects Velmora’s success, professionalism, and credibility.
The design must stand out while maintaining a polished, corporate tone. (bold, but understated)
The client just created a new logo, and the website design must be in sync with the logo design. Information about the logo colors, fonts, and message are in the attached design brief.
Updates

Target Market(s)

b2b: banks, brokers, institutional partners, vendors, and property sellers.

Industry/Entity Type

real estate investment company

Number of Pages Required

1 page

Font styles to use
Sans Serif

Colors

Designer to choose colors to be used in the design.

Requirements
Must have
• 1. homepage design (psd) 2. a top banner image (psd) for a default inner page
Nice to have
• please see attached design brief
Should not have

```html
<!DOCTYPE html>
<html lang="en">
<head>
<meta charset="utf-8">
<title>Velmora Partners</title>
<link href="https://fonts.googleapis.com/css2?family=Barlow+Semi+Condensed:wght@400;500;600;700&family=Lato:wght@400;700&display=swap" rel="stylesheet">
<style>
:root{
  --red:#dc1f26;
  --charcoal:#555150;
  --dark:#3f3b3a;
  --ink:#1e1e1e;
  --text:#3a3a3a;
  --muted:#5e5e5e;
  --paper:#ffffff;
  --wash:#f8f7f7;
  --blush:#fbeff0;
  --line:#d9d9d9;
}
*{margin:0;padding:0;box-sizing:border-box}
html,body{width:1200px;height:3039px;overflow:hidden}
body{position:relative;background:var(--paper);font-family:"Lato",sans-serif;color:var(--text)}
.abs{position:absolute}

/* top bar */
.topbar{left:0;top:0;width:1200px;height:71px;background:var(--paper)}
.mail{left:111px;top:18px;display:flex;align-items:center;gap:12px;font-size:20px;color:var(--muted);font-family:"Barlow Semi Condensed",sans-serif;font-weight:500}
.mail-dot{width:34px;height:34px;border-radius:50%;background:var(--charcoal);display:flex;align-items:center;justify-content:center}
.brand{left:0;width:1200px;top:8px;text-align:center;font-family:"Barlow Semi Condensed",sans-serif;font-weight:700;font-size:52px;letter-spacing:2px;color:var(--charcoal)}
.btn{display:inline-flex;align-items:center;justify-content:center;font-family:"Barlow Semi Condensed",sans-serif;font-weight:600;text-transform:uppercase;position:absolute;overflow:hidden}
.btn::before{content:"";position:absolute;left:0;top:0;width:0;height:0;border-top:22px solid var(--red);border-right:22px solid transparent}
.btn-dark{background:var(--charcoal);color:#fff}
.btn-light{background:#fff;color:var(--red)}
.quote{left:967px;top:14px;width:122px;height:42px;font-size:17px}

/* nav */
.nav{left:0;top:71px;width:1200px;height:68px;background:var(--charcoal)}
.nav a{position:absolute;top:0;height:68px;line-height:68px;color:#fff;text-decoration:none;font-family:"Barlow Semi Condensed",sans-serif;font-size:17px;letter-spacing:.5px}
.nav .active{background:var(--red);padding:0 39px 0 111px;left:0;font-weight:700}

/* hero */
.hero{left:0;top:139px;width:1200px;height:506px;background:linear-gradient(100deg,#4b4640 0%,#6d6254 35%,#9a8470 60%,#b7a38b 80%,#8e8a86 100%)}
.hero-shade{left:0;top:139px;width:700px;height:506px;background:linear-gradient(90deg,rgba(30,28,26,.6),rgba(30,28,26,0))}
.hero-title{left:110px;top:272px;font-family:"Barlow Semi Condensed",sans-serif;font-weight:700;font-size:38px;color:#fff;letter-spacing:1px}
.hero-text{left:111px;top:322px;width:490px;font-size:15.5px;line-height:26px;color:#fff}
.started{left:111px;top:442px;width:150px;height:52px;font-size:18px}

/* about */
.blush-tri{left:17px;top:667px}
.about-photo{left:111px;top:735px;width:403px;height:467px;background:linear-gradient(135deg,#27405f 0%,#5f7896 45%,#c8cfd6 70%,#e7e9ec 100%)}
.section-title{font-family:"Barlow Semi Condensed",sans-serif;font-weight:700;color:var(--charcoal);text-transform:uppercase;letter-spacing:.5px}
.section-title .tick{display:inline-block;width:0;height:0;border-top:14px solid var(--red);border-right:14px solid transparent;vertical-align:top;margin-right:4px;margin-top:6px}
.about-title{left:599px;top:726px;font-size:44px}
.about-body{left:599px;top:776px;width:489px;font-size:14px;line-height:25.8px;text-align:justify;color:var(--text)}
.about-body p+p{margin-top:25.8px}
.about-more{left:599px;top:1151px;width:150px;height:52px;font-size:17px}

/* stats */
.stat{width:330px;text-align:center}
.stat .num{font-family:"Barlow Semi Condensed",sans-serif;font-size:46px;color:var(--ink);font-weight:500}
.stat .cap{font-size:15.5px;line-height:26px;color:var(--ink)}
.divider{width:1px;height:225px;top:1283px;background:#f3c9cb}
.divider::after{content:"";position:absolute;left:-5px;top:106px;width:11px;height:11px;border-radius:50%;background:var(--red)}

/* strategy */
.strategy-bg{left:0;top:1572px;width:1200px;height:1084px;background:var(--wash)}
.strategy-title{left:0;width:1200px;top:1630px;text-align:center;font-size:46px;color:#fff}
.strategy-title .tick{border-top-color:#fff}
.card{width:306px;height:379px;top:1725px;background:#fff;box-shadow:0 2px 8px rgba(0,0,0,.12)}
.card .img{position:absolute;left:7px;top:7px;width:292px;height:249px}
.card .cut{position:absolute;left:7px;top:186px}
.card .icon{position:absolute;right:18px;top:212px}
.card h3{position:absolute;left:9px;top:268px;font-family:"Barlow Semi Condensed",sans-serif;font-weight:500;font-size:20px;color:var(--ink)}
.card p{position:absolute;left:9px;top:298px;width:285px;font-size:15px;line-height:26px;color:var(--ink)}
.arrow{width:32px;height:32px;border-radius:50%;border:2px solid;display:flex;align-items:center;justify-content:center}

/* apart */
.rule{left:111px;top:2200px;width:977px;height:1px;background:var(--line)}
.apart-title{left:0;width:1200px;top:2250px;text-align:center;font-size:46px}
.apart-body{left:200px;width:800px;top:2316px;text-align:center;font-size:15px;line-height:29.5px;color:var(--muted)}
.apart-body p+p{margin-top:29px}
.apart-more{left:525px;top:2522px;width:150px;height:51px;font-size:17px}

/* footer */
.footer{left:0;top:2656px;width:1200px;height:383px;background:var(--charcoal)}
.foot-brand{left:111px;top:2730px;font-family:"Barlow Semi Condensed",sans-serif;font-weight:700;font-size:86px;line-height:1;letter-spacing:3px;color:#fff}
.foot-info{left:111px;top:2834px;color:#fff;font-size:15.5px;line-height:32px}
.foot-info .row{display:flex;align-items:center;gap:10px}
.contact-title{left:567px;top:2736px;font-family:"Barlow Semi Condensed",sans-serif;font-weight:700;font-size:20px;color:#fff}
.field{background:#fff;font-size:13px;color:var(--text);padding:0 15px;display:flex;align-items:center}
.field.area{align-items:flex-start;padding-top:14px}
.submit{left:567px;top:2922px;width:150px;height:52px;font-size:17px}
</style>
</head>
<body>

<header>
  <div class="abs topbar"></div>
  <div class="abs mail">
    <span class="mail-dot"><svg width="18" height="13" viewBox="0 0 18 13"><rect x="1" y="1" width="16" height="11" fill="none" stroke="#fff" stroke-width="1.6"/><path d="M1 1l8 6 8-6" fill="none" stroke="#fff" stroke-width="1.6"/></svg></span>
    Mail Us: info@velmora.com
  </div>
  <div class="abs brand">VELMORA</div>
  <a class="btn btn-dark quote">Get a Quote</a>

  <nav class="abs nav">
    <a class="active">HOME</a>
    <a style="left:217px">OUR STORY</a>
    <a style="left:370px">INVESTMENT STRATEGY</a>
    <a style="left:607px">WHAT SETS US APART</a>
    <a style="left:830px">OUR PORTFOLIO</a>
    <a style="left:1021px">CONTACT</a>
  </nav>
</header>

<section>
  <div class="abs hero" role="img" aria-label="City skyline of downtown office towers under a blue sky"></div>
  <div class="abs hero-shade"></div>
  <h1 class="abs hero-title">EXPERIENCE - STRATEGY - VISION</h1>
  <p class="abs hero-text">Velmora Partners is a vertically integrated real estate investment firm with a proven four-decade track record. We acquire, reposition, and operate high-performing assets across multiple sectors - always with a focus on exceptional, risk-adjusted returns.</p>
  <a class="btn btn-light started">Get Started</a>
</section>

<section>
  <svg class="abs blush-tri" width="392" height="401" viewBox="0 0 392 401"><polygon points="0,0 392,0 0,401" fill="var(--blush)"/></svg>
  <div class="abs about-photo" role="img" aria-label="Two businessmen in suits shaking hands across a meeting table"></div>
  <h2 class="abs section-title about-title"><span class="tick"></span>About Velmora</h2>
  <div class="abs about-body">
    <p>Velmora Partners is a seasoned real estate investment and management firm with over 40 years of proven success in acquiring, repositioning, and operating properties across diverse asset classes. Our portfolio spans multifamily housing, skilled nursing facilities, and other strategic real estate investments throughout the United States.</p>
    <p>We take pride in our ability to identify undervalued or underperforming assets, implement targeted improvements, and enhance operational efficiency—unlocking long-term value for both our investors and the communities we serve. Our investment strategy combines rigorous market research, disciplined underwriting, and hands-on asset management to deliver consistent, risk-adjusted returns. With a commitment to integrity, innovation, and excellence, Velmora Partners fosters lasting relationships with residents, tenants, healthcare providers, and municipal stakeholders.</p>
  </div>
  <a class="btn btn-dark about-more">Read More</a>
</section>

<section>
  <div class="abs stat" style="left:108px;top:1320px"><div class="num">1989</div><div class="cap">Founded in 1989, with over three<br>decades of proven real estate<br>investment &amp; management expertise.</div></div>
  <div class="abs divider" style="left:468px"></div>
  <div class="abs stat" style="left:471px;top:1333px"><div class="num">23,000+</div><div class="cap">Multifamily &amp; healthcare units<br>under management</div></div>
  <div class="abs divider" style="left:805px"></div>
  <div class="abs stat" style="left:792px;top:1333px"><div class="num">$300+M</div><div class="cap">Million invested in property<br>renovations</div></div>
</section>

<section>
  <div class="abs strategy-bg"></div>
  <svg class="abs" style="left:0;top:1572px" width="1200" height="422" viewBox="0 0 1200 422"><polygon points="0,0 1200,0 0,422" fill="var(--red)"/></svg>
  <h2 class="abs section-title strategy-title"><span class="tick"></span>Our Investment Strategy</h2>

  <div class="abs arrow" style="left:36px;top:1899px;border-color:#fff"><svg width="16" height="14" viewBox="0 0 16 14"><path d="M15 7H2M7 1L1 7l6 6" fill="none" stroke="#fff" stroke-width="1.8"/></svg></div>
  <div class="abs arrow" style="left:1133px;top:1899px;border-color:var(--ink)"><svg width="16" height="14" viewBox="0 0 16 14"><path d="M1 7h13M9 1l6 6-6 6" fill="none" stroke="var(--ink)" stroke-width="1.8"/></svg></div>

  <article class="abs card" style="left:111px">
    <div class="img" role="img" aria-label="Hands holding a small model house" style="background:linear-gradient(160deg,#23364f,#4f6680 55%,#c9c4bb)"></div>
    <svg class="cut" width="292" height="70" viewBox="0 0 292 70"><polygon points="292,0 292,70 0,70" fill="#fff"/></svg>
    <svg class="icon" width="40" height="44" viewBox="0 0 40 44"><circle cx="24" cy="14" r="10" fill="none" stroke="var(--red)" stroke-width="3"/><circle cx="24" cy="14" r="3" fill="var(--red)"/><path d="M2 34l10-5h12l8-4v6l-10 7H6z" fill="var(--charcoal)"/></svg>
    <h3>Diversified Portfolio</h3>
    <p>We invest in multifamily housing, skilled nursing facilities, and other strategic real estate to balance opportunity and risk.</p>
  </article>
  <article class="abs card" style="left:447px">
    <div class="img" role="img" aria-label="Laptop with rising growth chart graphics" style="background:linear-gradient(160deg,#0f2a4a,#2c5583 50%,#9fb4c8)"></div>
    <svg class="cut" width="292" height="70" viewBox="0 0 292 70"><polygon points="292,0 292,70 0,70" fill="#fff"/></svg>
    <svg class="icon" width="44" height="44" viewBox="0 0 44 44"><circle cx="20" cy="24" r="13" fill="none" stroke="var(--charcoal)" stroke-width="6" stroke-dasharray="6 4"/><path d="M20 24L40 4M30 4h10v10" fill="none" stroke="var(--red)" stroke-width="4"/></svg>
    <h3>Value-Add Approach</h3>
    <p>We revitalize underperforming assets through renovations, efficiency improvements, and strong management.</p>
  </article>
  <article class="abs card" style="left:783px">
    <div class="img" role="img" aria-label="Hand ticking a digital checklist of data documents" style="background:linear-gradient(160deg,#1c1f24,#3b4654 55%,#8a8f96)"></div>
    <svg class="cut" width="292" height="70" viewBox="0 0 292 70"><polygon points="292,0 292,70 0,70" fill="#fff"/></svg>
    <svg class="icon" width="44" height="40" viewBox="0 0 44 40"><path d="M16 4a14 14 0 1 0 14 14H16z" fill="var(--charcoal)"/><path d="M20 0v14h14A14 14 0 0 0 20 0z" fill="var(--red)"/><rect x="30" y="22" width="12" height="3" fill="var(--red)"/><rect x="30" y="28" width="12" height="3" fill="var(--red)"/><rect x="30" y="34" width="12" height="3" fill="var(--red)"/></svg>
    <h3>Data-Driven Decisions</h3>
    <p>We revitalize underperforming assets through renovations, efficiency improvements, and strong management.</p>
  </article>
</section>

<section>
  <div class="abs rule"></div>
  <h2 class="abs section-title apart-title"><span class="tick"></span>What Sets Us Apart</h2>
  <div class="abs apart-body">
    <p>At Velmora Partners, we combine over four decades of real estate expertise with a hands-on approach to every investment. Our strength lies in identifying and transforming underperforming properties into thriving, high-value assets through strategic renovations, operational excellence, and careful market positioning.</p>
    <p>With a diverse portfolio spanning multifamily housing, skilled nursing facilities, and other strategic sectors, we balance opportunity and risk to deliver consistent, long-term returns.</p>
  </div>
  <a class="btn btn-dark apart-more">Read More</a>
</section>

<footer>
  <div class="abs footer"></div>
  <div class="abs foot-brand">VELMORA</div>
  <div class="abs foot-info">
    <div class="row"><svg width="16" height="12" viewBox="0 0 16 12"><rect width="16" height="12" fill="#fff"/><path d="M0 0l8 6 8-6" fill="none" stroke="var(--charcoal)" stroke-width="1.5"/></svg>Email Us: info@velmora.com</div>
    <div class="row"><svg width="10" height="14" viewBox="0 0 10 14"><path d="M5 0a5 5 0 0 1 5 5c0 4-5 9-5 9S0 9 0 5a5 5 0 0 1 5-5z" fill="#fff"/><circle cx="5" cy="5" r="2" fill="var(--charcoal)"/></svg>Location: Ridgeview, NJ</div>
    <div class="row"><svg width="13" height="13" viewBox="0 0 13 13"><rect width="13" height="13" fill="#fff"/></svg>Connectra:</div>
    <div>https://www.connectra.com/company/velmorapartners/</div>
    <div style="margin-top:3px">Copyrights@2025.Velmora.All Rights Reserved</div>
  </div>

  <div class="abs contact-title">CONTACT US</div>
  <div class="abs field" style="left:567px;top:2776px;width:166px;height:44px">Name</div>
  <div class="abs field" style="left:741px;top:2776px;width:165px;height:44px">Email</div>
  <div class="abs field" style="left:914px;top:2776px;width:174px;height:44px">Phone Number</div>
  <div class="abs field area" style="left:567px;top:2828px;width:521px;height:74px">Message</div>
  <a class="btn btn-light submit">Submit</a>
</footer>

</body>
</html>
```